Business Card Design

I am a mental health counselor in private practice. I provide counseling to individuals, couples, and adults. There is a design on CardLoom that I really like. It is 2 talking bubbles joined together by a heart. That is just a suggestion. I'm interested in other ideas. I would like my photo to be on the back of the card, along with the text Miriam Delacott Counseling. I would like mint green as my background color and navy writing, if possible. The final design should be elegant, professional, and maybe just a touch whimsical.
Target Market(s)
Individual adolescents, adults, couples, and families seeking counseling.
Industry/Entity Type
Mental Health
Contact Information for Business Card
Miriam Delacott
A Wholehearted Approach to Counseling
Miriam Delacott, M.S. NCC
Wexmoor Hall
2947 NW Calloway Street, Suite 318
Portland OR 97209
503-286-1573
counselingwithmiriam-example.com
Requirements
Must have
- The card must have all of the text provided and my photo.
Nice to have
- I like cards that are rounded on the sides, and I like thick paper.

```html
<!DOCTYPE html>
<html lang="en">
<head>
<meta charset="utf-8">
<title>Miriam Delacott Counseling — Business Card</title>
<link rel="stylesheet" href="https://fonts.googleapis.com/css2?family=Open+Sans:wght@400;600;700&display=swap">
<style>
  :root {
    --mint-bg: #cfeae2;
    --teal: #48c6bc;
    --teal-light: #56d0c5;
    --teal-deep: #1f8b79;
    --navy: #14233f;
    --white: #ffffff;
    --photo-light: #e9d9b4;
    --photo-dark: #2a2a2a;
  }
  * { box-sizing: border-box; margin: 0; padding: 0; }
  html, body {
    width: 1200px; height: 856px; overflow: hidden;
    background: var(--mint-bg);
    font-family: "Open Sans", Arial, sans-serif;
    color: var(--navy);
  }
  .canvas { position: relative; width: 1200px; height: 856px; }

  .card {
    position: absolute;
    width: 560px; height: 320px;
    border-radius: 34px;
    overflow: hidden;
    box-shadow: 0 10px 24px rgba(20, 60, 55, 0.18);
  }

  /* Front: contact side */
  .card-front { left: 560px; top: 90px; background: var(--white); }
  .brand {
    position: absolute; top: 52px; left: 0; right: 0;
    display: flex; justify-content: center; align-items: center; gap: 12px;
  }
  .brand-dot { width: 30px; height: 30px; border-radius: 50%; background: var(--teal-deep); }
  .brand-name { font-weight: 700; font-size: 22px; color: var(--navy); }
  .credentials { position: absolute; top: 122px; left: 0; right: 0; text-align: center; }
  .credentials .name { font-weight: 700; font-size: 17px; }
  .credentials .tagline { font-size: 14px; margin-top: 2px; }
  .contact-band {
    position: absolute; left: 0; right: 0; bottom: 0; height: 118px;
    background: var(--teal);
    display: flex; justify-content: space-between; align-items: flex-start;
    padding: 26px 34px 0;
    font-size: 13px; line-height: 1.6;
  }
  .contact-line { display: flex; align-items: center; gap: 8px; }
  .contact-line svg { width: 13px; height: 13px; flex: none; }
  .address { text-align: left; }

  /* Back: photo side */
  .card-back {
    left: 80px; top: 446px;
    background: linear-gradient(160deg, var(--teal-light), var(--teal));
  }
  .portrait {
    position: absolute; left: 40px; bottom: 0;
    width: 250px; height: 250px;
    border-radius: 46% 46% 0 0;
    background: linear-gradient(180deg, var(--photo-light) 0%, #d8c095 55%, var(--photo-dark) 100%);
  }
  .back-text {
    position: absolute; top: 40px; right: 36px; width: 300px;
    text-align: center;
  }
  .back-title { font-weight: 700; font-size: 21px; margin-bottom: 8px; }
  .quote { font-size: 14px; line-height: 1.45; }
</style>
</head>
<body>
<main class="canvas">

  <section class="card card-front" aria-label="Business card, contact side">
    <div class="brand">
      <span class="brand-dot"></span>
      <span class="brand-name">Miriam Delacott Counseling, LLC</span>
    </div>
    <div class="credentials">
      <p class="name">Miriam Delacott, M.S. NCC</p>
      <p class="tagline">A Wholehearted Approach to Counseling</p>
    </div>
    <div class="contact-band">
      <div class="contact">
        <p class="contact-line">
          <svg viewBox="0 0 24 24" aria-hidden="true"><path fill="#14233f" d="M6.6 10.8a15.1 15.1 0 0 0 6.6 6.6l2.2-2.2c.3-.3.7-.4 1-.2 1.1.4 2.3.6 3.6.6.6 0 1 .4 1 1V20c0 .6-.4 1-1 1A17 17 0 0 1 3 4c0-.6.4-1 1-1h3.5c.6 0 1 .4 1 1 0 1.3.2 2.5.6 3.6.1.3 0 .7-.2 1z"/></svg>
          503-286-1573
        </p>
        <p class="contact-line">
          <svg viewBox="0 0 24 24" aria-hidden="true"><rect x="2" y="4" width="20" height="16" rx="2" fill="#14233f"/><rect x="4" y="8" width="16" height="10" fill="#48c6bc"/></svg>
          counselingwithmiriam-example.com
        </p>
      </div>
      <address class="address" style="font-style:normal">
        Wexmoor Hall 2947 NW Calloway Street<br>
        Suite 318 Portland, OR 97209
      </address>
    </div>
  </section>

  <section class="card card-back" aria-label="Business card, photo side">
    <div class="portrait" role="img" aria-label="Portrait photo of Miriam Delacott"></div>
    <div class="back-text">
      <h1 class="back-title">Miriam Delacott Counseling</h1>
      <p class="quote">
        "Courage: To tell the story of<br>
        who you are with your whole heart."<br>
        Elena Whitcombe<br>
        What is your story?
      </p>
    </div>
  </section>

</main>
</body>
</html>
```